Bellcrest HVAC Business Card design

Looking for a modern professional two sided design. Showing contact info and services provided. Possibly on a silk card stock.
Using blues or greens or greys and maybe metallic. One color or a mixture of these.
Dorian Vance
dvance@bellcresthvac-example.net
555-318-4702
Air Conditioning
Heating
Heat Pumps / Gas / Oil
Ductless mini splits
Controls
VFD's
Pumps
Gas Fitting/Piping
Service and New install
Residential / Commercial
Industry/Entity Type
Mechanical HVAC
Contact Information for Business Card
Logo, contact info and provided services

```html
<!DOCTYPE html>
<html lang="en">
<head>
<meta charset="UTF-8">
<title>Bellcrest HVAC Business Card</title>
<link href="https://fonts.googleapis.com/css2?family=Roboto:wght@400;500;700;900&display=swap" rel="stylesheet">
<style>
  :root {
    --stage: #2b2e33;
    --card: #060606;
    --teal: #1fa88e;
    --white: #f4f4f4;
    --grey-text: #e6e6e6;
    --muted: #9a9a9a;
    --pattern-a: #2a2a2a;
    --pattern-b: #0a0a0a;
  }
  * { box-sizing: border-box; margin: 0; padding: 0; }
  html, body {
    width: 1200px; height: 900px; overflow: hidden;
    background: var(--stage);
    font-family: "Roboto", sans-serif;
  }
  .stage {
    width: 1200px; height: 900px;
    display: flex; flex-direction: column;
    align-items: center; justify-content: center; gap: 48px;
  }
  .card {
    position: relative;
    width: 630px; height: 360px;
    background: var(--card);
    border-radius: 22px;
    overflow: hidden;
    box-shadow: 0 14px 34px rgba(0,0,0,.45);
  }
  .brand {
    display: flex; align-items: center; gap: 12px;
    color: var(--teal);
    font-weight: 900;
    text-transform: uppercase;
    line-height: 1;
  }
  .brand-dot {
    flex: none;
    border: 4px solid var(--teal);
    border-radius: 50%;
  }
  .brand-name { display: flex; flex-direction: column; }
  .brand-name span + span { margin-top: 4px; }

  /* front */
  .card-front .brand {
    position: absolute; left: 36px; top: 96px;
    font-size: 34px; letter-spacing: .5px;
  }
  .card-front .brand-dot { width: 58px; height: 58px; }
  .services {
    position: absolute; left: 36px; top: 196px;
    width: 240px;
    list-style: none;
    display: flex; flex-wrap: wrap; gap: 3px 10px;
    font-size: 11px; line-height: 1.3;
    color: var(--muted);
  }
  .divider {
    position: absolute; left: 300px; top: 60px;
    width: 2px; height: 240px;
    background: var(--teal);
  }
  .contact {
    position: absolute; left: 324px; top: 74px;
    width: 290px;
    color: var(--grey-text);
  }
  .contact-name { font-size: 32px; font-weight: 900; color: var(--white); line-height: 1.1; }
  .contact-role { font-size: 20px; margin-top: 6px; }
  .contact-address { font-size: 16px; line-height: 1.4; margin-top: 10px; }
  .contact-line {
    display: flex; align-items: center; gap: 8px;
    font-size: 16px; margin-top: 6px;
    white-space: nowrap;
  }
  .contact-line svg { flex: none; }
  .contact-email { font-size: 14px; }

  /* back */
  .pattern {
    position: absolute; right: 0; top: 0;
    width: 390px; height: 360px;
    background: radial-gradient(ellipse at 65% 55%, var(--pattern-a), var(--pattern-b) 75%);
  }
  .card-back .brand {
    position: absolute; left: 60px; bottom: 56px;
    font-size: 30px;
  }
  .card-back .brand-dot { width: 50px; height: 50px; }
</style>
</head>
<body>
<main class="stage">
  <section class="card card-front" aria-label="Card front">
    <div class="brand">
      <span class="brand-dot"></span>
      <span class="brand-name"><span>Bellcrest</span><span>HVAC</span></span>
    </div>
    <ul class="services">
      <li>Air Conditioning</li><li>Heating</li><li>Heat Pumps / Gas / Oil</li>
      <li>Ductless mini splits</li><li>Controls</li><li>VFD's</li><li>Pumps</li>
      <li>Gas Fitting/Piping</li><li>Service and New install</li>
      <li>Residential / Commercial</li>
    </ul>
    <div class="divider"></div>
    <div class="contact">
      <p class="contact-name">Dorian Vance</p>
      <p class="contact-role">Director</p>
      <p class="contact-address">4180 Linden Ridge Dr. suite 210<br>Alder Falls, TX 75099</p>
      <p class="contact-line">
        <svg width="16" height="16" viewBox="0 0 24 24" aria-hidden="true"><path fill="#1fa88e" d="M6.6 10.8a15.1 15.1 0 0 0 6.6 6.6l2.2-2.2c.3-.3.7-.4 1-.2 1.1.4 2.3.6 3.6.6.6 0 1 .4 1 1V20c0 .6-.4 1-1 1A17 17 0 0 1 3 4c0-.6.4-1 1-1h3.5c.6 0 1 .4 1 1 0 1.3.2 2.5.6 3.6.1.3 0 .7-.2 1z"/></svg>
        <span>555-318-4702</span>
      </p>
      <p class="contact-line contact-email">
        <svg width="18" height="14" viewBox="0 0 24 18" aria-hidden="true"><rect x="1" y="1" width="22" height="16" fill="#1fa88e"/><path d="M1 1l11 9 11-9" fill="none" stroke="#060606" stroke-width="2"/></svg>
        <span>dvance@bellcresthvac-example.net</span>
      </p>
    </div>
  </section>

  <section class="card card-back" aria-label="Card back">
    <div class="pattern" role="img" aria-label="Faint repeating brand pattern in dark grey"></div>
    <div class="brand">
      <span class="brand-dot"></span>
      <span class="brand-name"><span>Bellcrest</span><span>HVAC</span></span>
    </div>
  </section>
</main>
</body>
</html>
```